BrivoMatex. Lantern for the Steady Growth. Business card

Professional business card for BrivoMatex (Lantern for the Steady Growth)
My rationale: Strategy-> Execution-> Results-> Value that lead to the BrivoMatex name: We put the Lantern for the Steady Growth.
We deliver value to our customers helping them at defining a good strategy (cyan arrow). 90% of well formulated strategies fail due to poor execution so we also consider strategical execution very important (green arrow). Due to the execution we obtain the results (blue arrow). Finally, the results provide feedback to redefine strategy, and the new strategy has to be executed and new results obtained providing new feedback and on and on. It's like a wheel that finally, must create corporate value: value for shareholders, staholders, employees, providers...-

Target Market(s)

CEOs and steering comitees , invewrnent funds

Industry/Entity Type

Business Consultant

Contact Information for Business Card

Tommaso Ferlini
CEO & Founder
tommaso.ferlini@brivomatex.example
Mobile: +34 611.205.938
www.brivomatex.example

Colors

Designer to choose colors to be used in the design.

Requirements
Nice to have
• Nice to hace the words: Strategy, execution, results
• Nice to vave the claim: Lantern for the Steady Growth
• The three colors should be shown:
• cyan for STRATEGY
• green for EXECUTION
• blue for RESULTS
Should not have
• Complete black background

```html
<!DOCTYPE html>
<html lang="en">
<head>
<meta charset="utf-8">
<title>BrivoMatex — Business Card</title>
<link href="https://fonts.googleapis.com/css2?family=Open+Sans:wght@400;600;700&display=swap" rel="stylesheet">
<style>
  :root {
    --stage: #e9ebef;
    --white: #ffffff;
    --paper: #f4f4f4;
    --navy: #26408f;
    --blue-deep: #22358a;
    --blue-light: #4f74bd;
    --cyan: #33a9d8;
    --green: #9cc653;
    --card-shadow: 0 18px 40px rgba(20, 30, 70, 0.25);
  }
  * { box-sizing: border-box; margin: 0; padding: 0; }
  html, body {
    width: 1200px; height: 900px; overflow: hidden;
    background: var(--stage);
    font-family: "Open Sans", Arial, sans-serif;
  }
  .sheet { position: relative; width: 1200px; height: 900px; }
  .card {
    position: absolute; left: 290px; width: 620px; height: 354px;
    border-radius: 18px; overflow: hidden; box-shadow: var(--card-shadow);
  }
  .card--front { top: 71px; }
  .card--back { top: 475px; }
  .card__art { position: absolute; inset: 0; width: 100%; height: 100%; display: block; }

  .brand {
    position: absolute; left: 34px; top: 178px;
    display: flex; align-items: center; gap: 8px;
    font-weight: 700; font-size: 32px; letter-spacing: -0.4px; line-height: 1.2;
    color: var(--navy);
  }
  .brand__dot { width: 12px; height: 12px; border-radius: 50%; background: var(--cyan); }

  .holder { position: absolute; right: 38px; top: 44px; text-align: right; color: var(--white); }
  .holder__name { font-weight: 700; font-size: 25px; letter-spacing: 0.6px; line-height: 1.1; }
  .holder__title { font-weight: 400; font-size: 18px; color: var(--cyan); letter-spacing: 0.6px; margin-top: 2px; }
  .holder__rule { width: 82px; height: 2px; background: var(--green); margin: 6px 0 0 auto; }

  .contacts { position: absolute; right: 30px; top: 190px; list-style: none; }
  .contacts__item {
    display: flex; align-items: center; justify-content: flex-end; gap: 12px;
    color: var(--white); font-size: 14px; letter-spacing: 0.3px; height: 34px;
  }
  .contacts__icon { width: 26px; height: 26px; flex: none; }

  .back-brand {
    position: absolute; left: 0; right: 0; top: 138px; text-align: center;
    font-weight: 700; font-size: 58px; letter-spacing: -0.5px; color: var(--white);
  }
  .back-web {
    position: absolute; right: 34px; bottom: 26px;
    font-size: 14px; letter-spacing: 0.8px; color: var(--white);
  }
</style>
</head>
<body>
<main class="sheet">

  <section class="card card--front" aria-label="Business card front">
    <svg class="card__art" viewBox="0 0 620 354" preserveAspectRatio="none" aria-hidden="true">
      <defs>
        <radialGradient id="frontBlue" cx="0.55" cy="0.75" r="0.8">
          <stop offset="0" stop-color="var(--blue-light)"/>
          <stop offset="1" stop-color="var(--blue-deep)"/>
        </radialGradient>
      </defs>
      <rect width="620" height="354" fill="url(#frontBlue)"/>
      <path d="M0 0 H330 C290 90 290 200 300 260 C296 300 280 330 260 354 H0 Z" fill="var(--green)"/>
      <path d="M0 0 H230 C300 60 320 160 300 250 C292 300 270 330 245 354 H0 Z" fill="var(--cyan)"/>
      <path d="M0 0 H160 C250 30 290 130 280 220 C274 290 240 330 210 354 H0 Z" fill="var(--paper)"/>
    </svg>

    <div class="brand"><span>BrivoMatex</span><span class="brand__dot"></span></div>

    <header class="holder">
      <h1 class="holder__name">Tommaso Ferlini</h1>
      <p class="holder__title">CEO &amp; Founder</p>
      <div class="holder__rule"></div>
    </header>

    <ul class="contacts">
      <li class="contacts__item">
        <span>+34 611.205.938</span>
        <svg class="contacts__icon" viewBox="0 0 26 26" aria-label="Phone">
          <circle cx="13" cy="13" r="13" fill="var(--white)"/>
          <rect x="9" y="6" width="8" height="14" rx="1.5" fill="none" stroke="var(--navy)" stroke-width="1.8"/>
          <circle cx="13" cy="17.2" r="0.9" fill="var(--navy)"/>
        </svg>
      </li>
      <li class="contacts__item">
        <span>www.brivomatex.example</span>
        <svg class="contacts__icon" viewBox="0 0 26 26" aria-label="Website">
          <circle cx="13" cy="13" r="13" fill="var(--white)"/>
          <circle cx="13" cy="13" r="6.5" fill="var(--navy)"/>
          <path d="M6.5 13 H19.5 M13 6.5 C10 9 10 17 13 19.5 M13 6.5 C16 9 16 17 13 19.5" stroke="var(--white)" stroke-width="0.9" fill="none"/>
        </svg>
      </li>
      <li class="contacts__item">
        <span>tommaso.ferlini@brivomatex.example</span>
        <svg class="contacts__icon" viewBox="0 0 26 26" aria-label="Email">
          <circle cx="13" cy="13" r="13" fill="var(--white)"/>
          <path d="M6.5 12.5 L19.5 7 L15 19.5 L12.5 14 Z" fill="var(--navy)"/>
        </svg>
      </li>
    </ul>
  </section>

  <section class="card card--back" aria-label="Business card back">
    <svg class="card__art" viewBox="0 0 620 354" preserveAspectRatio="none" aria-hidden="true">
      <defs>
        <radialGradient id="backBlue" cx="0.35" cy="0.6" r="0.85">
          <stop offset="0" stop-color="var(--blue-light)"/>
          <stop offset="1" stop-color="var(--blue-deep)"/>
        </radialGradient>
      </defs>
      <rect width="620" height="354" fill="url(#backBlue)"/>
    </svg>
    <div class="back-brand">BrivoMatex</div>
    <p class="back-web">www.brivomatex.example</p>
  </section>

</main>
</body>
</html>
```